Anzeigengestaltung für KFZ-Rundumservice
Zielgruppe
KFZ - Rundumservice
- Kundendienst aller Marken nach Herstellervorgabe
- Unfallinstandsetzung
- Karosseriearbeiten
- Lackierarbeiten
- Kundenersatzfahrzeuge
Ab sofort im Haus tägliche Hauptuntersuchung nach

```html
<!DOCTYPE html>
<html lang="de">
<head>
<meta charset="utf-8">
<title>Anzeige KFZ-Rundumservice</title>
<link href="https://fonts.googleapis.com/css2?family=Quicksand:wght@500;600;700&display=swap" rel="stylesheet">
<style>
  :root {
    --yellow: #fbd920;
    --dark: #48484a;
    --ink: #3a3a3c;
    --white: #ffffff;
    --page: #ffffff;
    --haze: #eef2f5;
    --steel: #8e959c;
    --engine: #2f3337;
    --skin: #d9a58a;
    --skin-shade: #b77e66;
    --sleeve: #24324a;
  }
  * { margin: 0; padding: 0; box-sizing: border-box; }
  html, body { width: 1200px; height: 1200px; overflow: hidden; background: var(--page); }
  body { font-family: "Quicksand", sans-serif; position: relative; }
  .ad {
    position: absolute; left: 155px; top: 197px; width: 894px; height: 832px;
    background: var(--white); overflow: hidden;
    box-shadow: 0 0 24px rgba(0,0,0,0.12);
  }
  .ad__photo {
    position: absolute; left: 0; top: 200px; width: 894px; height: 567px;
    background:
      radial-gradient(ellipse 260px 150px at 540px 140px, rgba(231,236,240,0.75), rgba(231,236,240,0) 70%),
      radial-gradient(ellipse 150px 110px at 800px 100px, var(--skin) 0%, rgba(217,165,138,0.6) 45%, rgba(217,165,138,0) 80%),
      radial-gradient(ellipse 190px 170px at 640px 440px, var(--skin) 0%, var(--skin-shade) 40%, rgba(183,126,102,0) 78%),
      radial-gradient(ellipse 140px 200px at 880px 420px, var(--sleeve) 0%, rgba(36,50,74,0.6) 50%, rgba(36,50,74,0) 85%),
      radial-gradient(ellipse 300px 140px at 520px 560px, rgba(240,243,246,0.9), rgba(240,243,246,0) 75%),
      linear-gradient(90deg, var(--haze) 0%, #e3e9ee 30%, var(--steel) 52%, #4f5459 68%, var(--engine) 100%);
  }
  .ad__shapes { position: absolute; left: 0; top: 0; width: 894px; height: 832px; }
  .kicker {
    position: absolute; left: 277px; top: 0; width: 336px; height: 59px;
    display: flex; align-items: center; justify-content: center;
    color: var(--yellow); font-weight: 700; font-size: 31px; letter-spacing: 0.3px;
  }
  .headline {
    position: absolute; left: 100px; width: 700px; top: 94px; text-align: center;
    color: var(--dark); font-weight: 700; font-size: 34px; line-height: 40px;
  }
  .phone {
    position: absolute; left: 300px; top: 190px; width: 390px; height: 56px;
    display: flex; align-items: center; justify-content: center;
    color: var(--yellow); font-weight: 700; font-size: 33px;
  }
  .service-title {
    position: absolute; left: 39px; top: 287px; height: 48px;
    display: flex; align-items: center;
    color: var(--white); font-weight: 700; font-size: 29px;
  }
  .services { position: absolute; left: 40px; top: 367px; list-style: none; }
  .services li {
    display: flex; align-items: flex-start; gap: 12px;
    color: var(--ink); font-weight: 700; font-size: 21px; line-height: 28px;
    margin-bottom: 19px;
  }
  .services svg { flex: none; margin-top: 6px; }
  .brand { position: absolute; left: 120px; top: 658px; }
  .brand__name { color: var(--yellow); font-weight: 700; font-size: 58px; line-height: 62px; letter-spacing: 1px; }
  .brand__line { color: var(--ink); font-weight: 500; font-size: 17px; margin-top: 2px; }
  .footer { position: absolute; left: 0; top: 767px; width: 894px; height: 65px; display: flex; }
  .footer__name {
    width: 447px; background: var(--dark); color: var(--white);
    display: flex; align-items: center; justify-content: center; font-weight: 700; font-size: 17px;
  }
  .footer__address {
    flex: 1; background: var(--yellow); color: var(--dark);
    display: flex; align-items: center; justify-content: center; font-weight: 700; font-size: 17px;
  }
</style>
</head>
<body>
  <main class="ad">
    <div class="ad__photo" role="img" aria-label="Foto: Mechaniker arbeitet mit Ratschenschlüssel im Motorraum"></div>

    <svg class="ad__shapes" viewBox="0 0 894 832" aria-hidden="true">
      <path class="header-band" d="M290 0 H894 V203 H330 C200 203 120 240 85 290 H0 V210 C15 110 140 40 290 0 Z" fill="var(--yellow)"/>
      <path class="header-edge" d="M85 290 C120 240 200 203 330 203 H894" fill="none" stroke="var(--dark)" stroke-width="3"/>
      <path class="header-top" d="M0 210 C15 110 140 40 290 0" fill="none" stroke="var(--dark)" stroke-width="3"/>
      <path class="kicker-tab" d="M277 0 H613 L593 47 Q588 59 575 59 H315 Q302 59 297 47 Z" fill="var(--dark)"/>
      <path class="phone-pill" d="M262 190 H680 Q691 190 691 201 V235 Q691 246 680 246 H262 Z" fill="var(--dark)"/>
      <circle cx="268" cy="218" r="32" fill="var(--yellow)" stroke="var(--dark)" stroke-width="5"/>
      <path class="phone-icon" d="M256 203 l6 -3 5 9 -4 3 q3 8 9 13 l4 -3 7 7 -4 5 q-12 2 -22 -14 q-6 -10 -1 -17 z" fill="var(--dark)"/>
      <path d="M272 201 q8 2 11 10 M274 194 q14 3 17 17" fill="none" stroke="var(--dark)" stroke-width="2.5" stroke-linecap="round"/>
      <path class="service-bar" d="M0 287 H429 L405 322 Q396 335 382 335 H0 Z" fill="var(--dark)"/>
    </svg>

    <div class="kicker">AB SOFORT:</div>
    <h1 class="headline">Tägliche Hauptuntersuchung im Haus<br>nach § 29 Stvzo</h1>
    <div class="phone">Telefon 07000-4821</div>

    <h2 class="service-title">KFZ - Rundumservice</h2>
    <ul class="services">
      <li><svg width="18" height="18" viewBox="0 0 18 18"><circle cx="9" cy="9" r="7.5" fill="none" stroke="var(--ink)" stroke-width="2"/><path d="M5 9 l3 3 l8 -9" fill="none" stroke="var(--ink)" stroke-width="2.2" stroke-linecap="round"/></svg><span>Kundendienst aller Marken<br>nach Herstellervorgabe</span></li>
      <li><svg width="18" height="18" viewBox="0 0 18 18"><circle cx="9" cy="9" r="7.5" fill="none" stroke="var(--ink)" stroke-width="2"/><path d="M5 9 l3 3 l8 -9" fill="none" stroke="var(--ink)" stroke-width="2.2" stroke-linecap="round"/></svg><span>Unfallinstandsetzung</span></li>
      <li><svg width="18" height="18" viewBox="0 0 18 18"><circle cx="9" cy="9" r="7.5" fill="none" stroke="var(--ink)" stroke-width="2"/><path d="M5 9 l3 3 l8 -9" fill="none" stroke="var(--ink)" stroke-width="2.2" stroke-linecap="round"/></svg><span>Karosseriearbeiten</span></li>
      <li><svg width="18" height="18" viewBox="0 0 18 18"><circle cx="9" cy="9" r="7.5" fill="none" stroke="var(--ink)" stroke-width="2"/><path d="M5 9 l3 3 l8 -9" fill="none" stroke="var(--ink)" stroke-width="2.2" stroke-linecap="round"/></svg><span>Lackierarbeiten</span></li>
      <li><svg width="18" height="18" viewBox="0 0 18 18"><circle cx="9" cy="9" r="7.5" fill="none" stroke="var(--ink)" stroke-width="2"/><path d="M5 9 l3 3 l8 -9" fill="none" stroke="var(--ink)" stroke-width="2.2" stroke-linecap="round"/></svg><span>Kundenersatzfahrzeuge</span></li>
    </ul>

    <div class="brand">
      <div class="brand__name">BRENNER</div>
      <div class="brand__line">Autolackierung &amp; Karosserietechnik</div>
    </div>

    <footer class="footer">
      <div class="footer__name">Autolackierung &amp; Karosserietechnik Brenner</div>
      <div class="footer__address">Werkstraße 14 | 73500 Talheim</div>
    </footer>
  </main>
</body>
</html>
```